Business card design needed

Our modern electrical contracting company requires business card design utilising our logo and incorporating our tag line "Service when you need it". We specialise in assisting our customers 24/7 offering a breakdown service.

Industry/Entity Type

Electrical

Contact Information for Business Card

Marcus Penfold, Electrical contractor,Tel: (08) 8546 3071, Fax: (08) 8679 4305, Mob 0428 736 514, Email: marcus.penfold@brightwirepower.com.au, Web: www.brightwirepower.com.au

Requirements
Must have
• we require a 2 sided card.
Front- Logo, tag line and contact information.
Rear- service when you need it! Call now for our 24/7 breakdown service

```html
<!DOCTYPE html>
<html lang="en">
<head>
<meta charset="utf-8">
<title>Brightwire Power – Business Card Concepts</title>
<link href="https://fonts.googleapis.com/css2?family=Arimo:wght@400;700&family=Open+Sans:ital,wght@0,400;0,600;1,700&display=swap" rel="stylesheet">
<style>
  :root {
    --stage: #5a3a22;
    --label: #1c120b;
    --card: #ffffff;
    --brand-blue: #2c58a8;
    --navy-text: #2a3585;
    --body-text: #333333;
    --band: #3a3583;
    --band-text: #ffffff;
    --divider: #b9b9b9;
    --mark: #2f62b5;
    --mark-faint: #e6e7ea;
    --deep-top: #3f77c3;
    --deep-bottom: #1f4290;
  }
  * { box-sizing: border-box; margin: 0; padding: 0; }
  html, body { width: 1200px; height: 788px; overflow: hidden; background: var(--stage); }
  .stage { position: relative; width: 1200px; height: 788px; font-family: "Arimo", Arial, sans-serif; }

  .view-label {
    position: absolute; width: 525px; text-align: center;
    font-family: "Open Sans", Arial, sans-serif; font-size: 21px; color: var(--label);
  }

  .card {
    position: absolute; width: 525px; height: 299px; border-radius: 20px;
    background: var(--card); overflow: hidden;
    box-shadow: 0 6px 14px rgba(0,0,0,.45);
  }
  .card--front { left: 54px; top: 75px; }
  .card--back-1 { left: 622px; top: 75px; }
  .card--back-2 { left: 54px; top: 446px; }
  .card--back-3 { left: 622px; top: 446px; background: linear-gradient(var(--deep-top), var(--deep-bottom)); }

  .brand-dot { position: absolute; border-radius: 50%; background: var(--mark); }
  .brand-name {
    position: absolute; font-weight: 700; color: var(--brand-blue);
    white-space: nowrap; text-align: center; letter-spacing: .2px;
  }

  /* front */
  .card--front .brand-dot { left: 122px; top: 64px; width: 72px; height: 72px; }
  .card--front .brand-name { left: 0; width: 317px; top: 150px; font-size: 25px; }
  .front-divider { position: absolute; left: 312px; top: 25px; width: 2px; height: 200px;
    background: linear-gradient(transparent, var(--divider), transparent); }
  .contact { position: absolute; left: 339px; top: 55px; font-family: "Open Sans", Arial, sans-serif; color: var(--body-text); }
  .contact__name { font-family: "Arimo", Arial, sans-serif; font-size: 18px; color: var(--navy-text); line-height: 22px; }
  .contact__role { font-family: "Arimo", Arial, sans-serif; font-size: 14px; color: var(--navy-text); line-height: 18px; margin-bottom: 15px; }
  .contact__line { font-size: 12.5px; line-height: 26.5px; }
  .contact__key { font-weight: 700; font-style: italic; }
  .front-tagline { position: absolute; left: 0; width: 525px; top: 237px; text-align: center;
    font-size: 14px; color: var(--body-text); }
  .front-band { position: absolute; left: 0; bottom: 0; width: 100%; height: 39px; background: var(--band);
    color: var(--band-text); font-family: "Open Sans", Arial, sans-serif; font-size: 12px;
    display: flex; align-items: center; justify-content: center; gap: 6px; }
  .front-band b { font-style: italic; }

  /* backs */
  .back-tagline { position: absolute; left: 0; width: 525px; text-align: center;
    font-size: 14px; line-height: 17px; color: var(--navy-text); }
  .card--back-1 .brand-dot { left: 202px; top: 20px; width: 120px; height: 120px; }
  .card--back-1 .brand-name { left: 0; width: 525px; top: 162px; font-size: 40px; }
  .card--back-1 .back-tagline { top: 247px; }

  .card--back-2 .brand-dot { left: 164px; top: 30px; width: 200px; height: 200px; background: var(--mark-faint); }
  .card--back-2 .brand-name { left: 0; width: 525px; top: 126px; font-size: 44px; }
  .card--back-2 .back-tagline { top: 246px; }

  .card--back-3 .brand-dot { left: 208px; top: 31px; width: 112px; height: 112px; background: #e9eef7; }
  .card--back-3 .brand-name { left: 0; width: 525px; top: 165px; font-size: 38px; color: #ffffff; }
  .card--back-3 .back-tagline { top: 246px; color: #ffffff; }
</style>
</head>
<body>
<div class="stage">
  <div class="view-label" style="left:54px; top:32px;">Front</div>
  <div class="view-label" style="left:622px; top:32px;">Back - 1</div>
  <div class="view-label" style="left:54px; top:403px;">Back - 2</div>
  <div class="view-label" style="left:622px; top:403px;">Back - 3</div>

  <section class="card card--front">
    <div class="brand-dot"></div>
    <div class="brand-name">BRIGHTWIRE POWER</div>
    <div class="front-divider"></div>
    <div class="contact">
      <div class="contact__name">Marcus Penfold</div>
      <div class="contact__role">Electrical contractor</div>
      <div class="contact__line"><span class="contact__key">cell</span> : 0428 736 514</div>
      <div class="contact__line"><span class="contact__key">phone</span> : (08) 8546 3071</div>
      <div class="contact__line"><span class="contact__key">fax</span> : (08) 8679 4305</div>
    </div>
    <div class="front-tagline">Service when you need it</div>
    <div class="front-band">
      <span><b>web</b> : www.brightwirepower.com.au</span><span>|</span>
      <span><b>email</b> : marcus.penfold@brightwirepower.com.au</span>
    </div>
  </section>

  <section class="card card--back-1">
    <div class="brand-dot"></div>
    <div class="brand-name">BRIGHTWIRE POWER</div>
    <p class="back-tagline">service when you need it!<br>Call now for our 24/7 breakdown service</p>
  </section>

  <section class="card card--back-2">
    <div class="brand-dot"></div>
    <div class="brand-name">BRIGHTWIRE POWER</div>
    <p class="back-tagline">service when you need it!<br>Call now for our 24/7 breakdown service</p>
  </section>

  <section class="card card--back-3">
    <div class="brand-dot"></div>
    <div class="brand-name">BRIGHTWIRE POWER</div>
    <p class="back-tagline">service when you need it!<br>Call now for our 24/7 breakdown service</p>
  </section>
</div>
</body>
</html>
```